Corvanta Stationery Design

We need design for our stationary, including:
1) Letterhead
- A4/Letter size in landscape and portrait letterhead
- The letterhead must be in a word file, and the address should be editable using the Felixti or Perpetua Titling TTF
- The output file should be in .docx and in .ai.
2) Business card
- The business card will be printed in white paper and single face only, so there should be nothing on the reverse side.
3) Envelope (sizes A4, Letter, and small document)
Please refer to the picture showing some samples of stationary with designs that would fulfill our wish.
We're including the logo in .AI.
Thanks
Target Market(s)
High end investors
Industry/Entity Type
Landscape
Look and feel
Each slider illustrates characteristics of the customer's brand and the style your logo design should communicate.

```html
<!DOCTYPE html>
<html lang="en">
<head>
<meta charset="utf-8">
<title>Corvanta Capital Partners — Stationery</title>
<link href="https://fonts.googleapis.com/css2?family=Cinzel:wght@400&family=Questrial&family=Roboto:wght@700&display=swap" rel="stylesheet">
<style>
  :root {
    --bg: #efefef;
    --paper: #ffffff;
    --paper-edge: #e2e2e2;
    --brand: #5b6671;
    --accent: #1a78a6;
    --ink: #3c3c3c;
    --muted: #c9c9c9;
    --window: #e6e6e6;
  }
  * { box-sizing: border-box; margin: 0; padding: 0; }
  html, body { width: 1200px; height: 924px; overflow: hidden; background: var(--bg); }
  body { position: relative; font-family: "Questrial", sans-serif; color: var(--ink); }

  .sheet-notes { position: absolute; left: 26px; top: 30px; color: var(--muted); font-size: 10px; line-height: 12px; }
  .sheet-notes h1 { font-family: "Roboto", sans-serif; font-weight: 700; font-size: 15px; margin-bottom: 22px; letter-spacing: .5px; }
  .sheet-notes h2 { font-family: "Roboto", sans-serif; font-weight: 700; font-size: 11px; line-height: 13px; margin-bottom: 22px; }
  .sheet-notes p { margin-bottom: 12px; }
  .sheet-notes ul { list-style: none; margin-bottom: 14px; }

  .piece { position: absolute; background: var(--paper); border: 1px solid var(--paper-edge); overflow: hidden; }

  .wordmark { position: absolute; text-align: center; font-family: "Cinzel", serif; color: var(--brand); font-weight: 400; line-height: 1; white-space: nowrap; }
  .wordmark .name { display: block; }
  .wordmark .tag { display: block; letter-spacing: .18em; }

  .letterhead { left: 222px; top: 98px; width: 356px; height: 504px; }
  .letterhead .wordmark { left: 205px; width: 130px; top: 28px; }
  .letterhead .name { font-size: 19px; letter-spacing: .05em; }
  .letterhead .tag { font-size: 7px; margin-top: 3px; }
  .letterhead-footer { position: absolute; left: 0; right: 0; bottom: 9px; text-align: center; font-family: "Cinzel", serif; font-size: 4.6px; line-height: 7px; color: var(--ink); white-space: nowrap; }
  .letterhead-footer .company { font-size: 5.6px; margin-bottom: 4px; }

  .folder { left: 640px; top: 75px; width: 420px; height: 531px; }
  .folder-edge { position: absolute; top: 0; bottom: 0; width: 1px; background: var(--paper-edge); }
  .folder .wordmark { left: 188px; width: 180px; top: 76px; }
  .folder .name { font-size: 28px; letter-spacing: .05em; }
  .folder .tag { font-size: 9.5px; margin-top: 4px; }
  .folder-web { position: absolute; left: 188px; width: 180px; text-align: center; top: 498px; font-family: "Cinzel", serif; font-size: 8.5px; letter-spacing: .18em; color: var(--ink); }

  .card { width: 160px; height: 91px; left: 95px; }
  .card .wordmark { width: 80px; }
  .card .name { font-size: 13px; letter-spacing: .04em; }
  .card .tag { font-size: 4.6px; margin-top: 2px; }
  .card-a { top: 646px; }
  .card-a .wordmark { left: 68px; top: 13px; }
  .card-a .person { position: absolute; left: 9px; top: 57px; font-size: 5.4px; line-height: 6.5px; }
  .card-a .contact { position: absolute; left: 9px; top: 74px; font-size: 3.8px; line-height: 5.5px; white-space: nowrap; }
  .card-b { top: 763px; }
  .card-b .wordmark { left: 12px; top: 19px; }
  .card-b .person { position: absolute; right: 9px; top: 54px; text-align: right; font-size: 5.4px; line-height: 6.5px; }
  .card-b .contact-row { position: absolute; left: 8px; right: 8px; top: 74px; display: flex; justify-content: space-between; font-size: 3.6px; line-height: 5px; white-space: nowrap; }
  .card-b .contact-row div + div { border-left: 1px solid var(--muted); padding-left: 4px; }
  .label { color: var(--accent); }
  .person strong { font-weight: 700; font-family: "Roboto", sans-serif; }
  .role { font-style: normal; color: #777; }

  .envelope-window { left: 297px; top: 660px; width: 370px; height: 190px; }
  .envelope-window .address-window { position: absolute; left: 57px; top: 107px; width: 155px; height: 53px; background: var(--window); border-radius: 5px; }
  .envelope-window .wordmark { left: 242px; width: 122px; top: 108px; }
  .envelope-window .name { font-size: 18px; letter-spacing: .04em; }
  .envelope-window .tag { font-size: 6.4px; margin-top: 3px; }
  .envelope-window .return-address { position: absolute; left: 242px; width: 122px; top: 151px; text-align: center; font-family: "Cinzel", serif; font-size: 4.4px; line-height: 6px; white-space: nowrap; }

  .envelope-flap { left: 733px; top: 660px; width: 399px; height: 190px; }
  .envelope-flap svg { position: absolute; left: -1px; top: -1px; }
  .envelope-flap .wordmark { left: 150px; width: 100px; top: 27px; color: var(--paper); }
  .envelope-flap .name { font-size: 11px; letter-spacing: .05em; }
  .envelope-flap .tag { font-size: 4px; margin-top: 1px; }
</style>
</head>
<body>

  <aside class="sheet-notes">
    <h1>STATIONERY #1</h1>
    <h2>CORVANTA<br>CAPITAL PARTNERS</h2>
    <p>MAIN LAYOUT:</p>
    <ul>
      <li>- Letterhead</li>
      <li>- Paper Folder</li>
      <li>- Envelope</li>
      <li>- Business cards</li>
    </ul>
    <p>ADDITIONAL ITEMS:</p>
    <ul>
      <li>- Envelope DL, C5, C4</li>
      <li>- Continuation Letterhead</li>
    </ul>
  </aside>

  <section class="piece letterhead">
    <div class="wordmark"><span class="name">CORVANTA</span><span class="tag">CAPITAL PARTNERS</span></div>
    <footer class="letterhead-footer">
      <div class="company">CORVANTA CAPITAL PARTNERS, LLC</div>
      <div>218 HARLOW STREET, 3RD FLOOR, ASHFORD, CALIFORNIA 90210</div>
      <div>PHONE 415.555.0142 • FAX 415.555.0143 • EMAIL INFO@CORVANTA.COM • WWW.CORVANTA.COM</div>
    </footer>
  </section>

  <section class="piece folder">
    <span class="folder-edge" style="left:10px"></span>
    <span class="folder-edge" style="left:16px"></span>
    <span class="folder-edge" style="left:22px"></span>
    <div class="wordmark"><span class="name">CORVANTA</span><span class="tag">CAPITAL PARTNERS</span></div>
    <div class="folder-web">WWW.CORVANTA.COM</div>
  </section>

  <section class="piece card card-a">
    <div class="wordmark"><span class="name">CORVANTA</span><span class="tag">CAPITAL PARTNERS</span></div>
    <div class="person"><strong>DANIEL WHITMORE</strong><br><span class="role">Chairman</span></div>
    <div class="contact">218 Harlow Street 3rd Floor, Ashford, CA 90210<br>
      <span class="label">Phone:</span> 415.555.0142 | <span class="label">Fax:</span> 415.555.0143 | www.corvanta.com</div>
  </section>

  <section class="piece card card-b">
    <div class="wordmark"><span class="name">CORVANTA</span><span class="tag">CAPITAL PARTNERS</span></div>
    <div class="person"><strong>DANIEL WHITMORE</strong><br><span class="role">Chairman</span></div>
    <div class="contact-row">
      <div>218 Harlow St 3rd Fl<br>Ashford, CA 90210</div>
      <div><span class="label">Phone:</span> 415.555.0142<br><span class="label">Fax:</span> 415.555.0143</div>
      <div><span class="label">Email:</span> info@corvanta.com<br><span class="label">Web:</span> corvanta.com</div>
    </div>
  </section>

  <section class="piece envelope-window">
    <div class="address-window"></div>
    <div class="wordmark"><span class="name">CORVANTA</span><span class="tag">CAPITAL PARTNERS</span></div>
    <div class="return-address">218 HARLOW STREET, 3RD FLOOR<br>ASHFORD, CALIFORNIA 90210</div>
  </section>

  <section class="piece envelope-flap">
    <svg width="401" height="70" viewBox="0 0 401 70" aria-hidden="true">
      <path d="M0 0 H401 L393 62 Q392 68 386 68 H15 Q9 68 8 62 Z" fill="var(--accent)"/>
    </svg>
    <div class="wordmark"><span class="name">CORVANTA</span><span class="tag">CAPITAL PARTNERS</span></div>
  </section>

</body>
</html>
```